Tidewell Works's Facebook Cover Design

I am in need of a social media cover for my company's Facebook account. Please leverage the green logos and color palette attached.

Tidewell Works offers 2 primary services:
1.) Business Automation Services
2.) AI (artificial intelligence integrations)

While a lot of what we do is highly technical, what we deliver is not. In a nutshell, we help our clients to connect their data regardless of what application that data is sitting in. Because we can connect that data, often times we can:

A.) offer more intelligent marketing and help our client increase their revenue.
B.) automate highly repetitive tasks using technology and drive down their costs thus saving them money
C.) help our clients use AI to better serve their customers

You can read a little bit about our company here: https://www.tidewellworks.example

Our tagline is: "Connect data to increase the flow of profitability."

Visually, we'd like your help to illustrate the "connecting" of these applications. Please let me know if you have any questions.

Target Market(s)

Business Owners or Marketing Managers

Industry/Entity Type

Marketing technologies.

Font styles to use
Sans Serif

Requirements
Must have
• Please make every effort to have the cover compatible with the color palette of the attached images.
Should not have
• Please do not use the standard clipart or stock libraries of AI = robot. If you do, please make them small. We help business glue their data from different sources to solve real work problems. Little robots are overused.

```html
<!DOCTYPE html>
<html lang="en">
<head>
<meta charset="utf-8">
<title>Tidewell Works – Facebook Cover</title>
<link href="https://fonts.googleapis.com/css2?family=Montserrat:ital,wght@0,500;0,700;0,800;1,400&display=swap" rel="stylesheet">
<style>
  :root {
    --stage: #3f3f3f;
    --navy: #0e1f3a;
    --navy-deep: #0b1a31;
    --photo-blue: #1d5a9c;
    --photo-cyan: #3fb6e8;
    --green: #8cc63f;
    --white: #ffffff;
  }
  * { box-sizing: border-box; margin: 0; padding: 0; }
  html, body {
    width: 1200px; height: 1043px; overflow: hidden;
    background: var(--stage);
    font-family: "Montserrat", sans-serif;
  }
  .cover {
    position: absolute; left: 0; top: 258px;
    width: 1200px; height: 526px;
    background: var(--navy);
    overflow: hidden;
  }
  .cover__photo {
    position: absolute; left: 0; top: 0;
    width: 700px; height: 526px;
    background:
      radial-gradient(ellipse at 40% 45%, rgba(63,182,232,0.45), rgba(63,182,232,0) 60%),
      linear-gradient(90deg, var(--photo-blue) 0%, #16437a 55%, var(--navy) 100%);
  }
  .cover__content {
    position: absolute; right: 64px; top: 0;
    width: 560px; height: 526px;
    text-align: right; color: var(--white);
  }
  .brand {
    position: absolute; right: 0; top: 62px;
    display: flex; align-items: center; gap: 12px;
  }
  .brand__dot {
    width: 22px; height: 22px; border-radius: 50%;
    background: var(--green);
  }
  .brand__name {
    font-weight: 800; font-size: 44px; letter-spacing: -1px;
    color: var(--white); white-space: nowrap;
  }
  .brand__rule {
    position: absolute; right: 0; top: 146px;
    width: 126px; height: 4px; background: var(--green);
  }
  .headline {
    position: absolute; right: 0; top: 168px;
    font-weight: 700; font-size: 32px; line-height: 42px;
    letter-spacing: 1.5px; white-space: nowrap;
  }
  .headline__strong { font-weight: 800; display: block; }
  .headline__accent { color: var(--green); }
  .benefits {
    position: absolute; right: 0; top: 256px;
    list-style: none;
    font-style: italic; font-weight: 400; font-size: 18px;
    line-height: 20.5px; letter-spacing: 0.6px;
  }
  .benefits li::after {
    content: ""; display: inline-block;
    width: 5px; height: 5px; border-radius: 50%;
    background: var(--white); margin-left: 6px; vertical-align: middle;
  }
  .web {
    position: absolute; right: 0; top: 434px;
    background: var(--green); color: var(--white);
    font-weight: 500; font-size: 19px; letter-spacing: 0.6px;
    padding: 2px 8px; line-height: 23px;
  }
  .web b { font-weight: 800; }
</style>
</head>
<body>
  <section class="cover">
    <div class="cover__photo" role="img" aria-label="Photo of hands typing on a laptop overlaid with glowing blue data charts and connected application nodes"></div>
    <div class="cover__content">
      <div class="brand">
        <span class="brand__dot"></span>
        <span class="brand__name">Tidewell Works</span>
      </div>
      <div class="brand__rule"></div>
      <h1 class="headline">
        CONNECT YOUR <span class="headline__accent">DATA</span> TO
        <span class="headline__strong">INCREASE PROFITS</span>
      </h1>
      <ul class="benefits">
        <li>Grow your revenue</li>
        <li>Reduce costs</li>
        <li>Increase customer communications</li>
        <li>Increase data accuracy</li>
        <li>Improve customer retention</li>
      </ul>
      <div class="web">www.<b>tidewellworks</b>.example</div>
    </div>
  </section>
</body>
</html>
```